Vardel Precision New Website Design

We just changed our logo (thank you ArtFolkly) and company name change from Vardel Precision Machining to Vardel Precision Manufacturing. We do CNC Swiss screw machining and multi-axis machines. We make parts for many industries. We make large quantity production parts as well small R&D quantities. You can look at our current (outdated) website: http://www.vardelprecisionmachining.example to see what we do. We would like a WordPress site, including contact form for "request for quote" . We would also like it to be mobile friendly, and the ability to maintain it ourselves after it is finished I have included our new logo and fonts for references. We would like our site to convey the feeling of precision, capability, and trust worthiness with a very modern look. The new website address is www.vardelprec-mfg.example

Font styles to use
Serif
Sans Serif
Other font styles liked:
• fronts included, not sure if they work

Colors

Designer to choose colors to be used in the design.

Requirements
Must have
• Contact Info, request for quote field

```html
<!DOCTYPE html>
<html lang="en">
<head>
<meta charset="utf-8">
<title>Vardel Precision Manufacturing</title>
<link href="https://fonts.googleapis.com/css2?family=Montserrat:wght@300;400;600;700&family=Open+Sans:wght@400;600;700&display=swap" rel="stylesheet">
<style>
:root{
  --navy:#1f3b8c;
  --navy-dark:#15296a;
  --ink:#3a3d45;
  --text:#555a63;
  --muted:#8a8f98;
  --line:#d9dce2;
  --grey-bg:#eef0f4;
  --white:#ffffff;
  --footer:#3b3e46;
  --footer-text:#c9ccd2;
}
*{box-sizing:border-box;margin:0;padding:0}
html,body{width:1200px;height:4775px;overflow:hidden}
body{font-family:"Open Sans",Arial,sans-serif;color:var(--text);background:var(--white);position:relative}
.section{position:absolute;left:0;width:1200px}
.abs{position:absolute}
.heading{font-family:"Montserrat",Arial,sans-serif;font-weight:300;font-size:38px;letter-spacing:2px;color:var(--ink);text-align:center;width:100%}
.heading strong{font-weight:700}
.subheading{font-family:"Montserrat",Arial,sans-serif;font-weight:600;font-size:14px;color:var(--ink);text-align:center;width:100%}
.dots{display:flex;gap:7px;justify-content:center;width:100%}
.dots span{width:6px;height:6px;border-radius:50%;background:var(--navy)}
.dots span:nth-child(1),.dots span:nth-child(5){opacity:.35;width:5px;height:5px;margin-top:.5px}
.dots span:nth-child(2),.dots span:nth-child(4){opacity:.65}
.btn{display:inline-block;border:2px solid var(--navy);border-radius:20px;font-family:"Montserrat",Arial,sans-serif;font-weight:600;font-size:12px;letter-spacing:1px;color:var(--navy);padding:9px 22px;background:var(--white)}

/* header + hero */
.site-header{top:0;height:80px;background:rgba(255,255,255,.96);z-index:3}
.brand{left:135px;top:22px;display:flex;align-items:center;gap:10px;font-family:"Montserrat",Arial,sans-serif;font-weight:700;font-size:20px;color:var(--navy)}
.brand i{width:28px;height:28px;border-radius:50%;border:3px solid var(--navy);display:block}
.nav{right:135px;top:28px;display:flex;gap:6px;font-family:"Montserrat",Arial,sans-serif;font-weight:600;font-size:12px;color:var(--ink)}
.nav span{padding:6px 10px}
.nav .active{background:var(--grey-bg);color:var(--navy)}
.hero{top:0;height:640px;overflow:hidden}
.hero-photo{left:0;top:0;width:1200px;height:640px;background:linear-gradient(100deg,#f4f6fa 0%,#dfe5ee 38%,#8c9db7 68%,#3f5272 100%)}
.hero-title{left:143px;top:152px;font-family:"Montserrat",Arial,sans-serif;font-weight:300;font-size:40px;line-height:46px;color:var(--ink);letter-spacing:1px}
.hero-title strong{font-weight:700;color:var(--navy)}
.hero-text{left:143px;top:306px;width:470px;font-size:14px;line-height:20px;color:var(--ink)}
.hero .btn{position:absolute;left:143px;top:380px}

/* about */
.about{top:640px;height:690px}
.about .heading{top:110px}
.about .subheading{top:163px}
.about .dots{top:192px}
.about-intro{left:143px;top:218px;width:914px;text-align:center;font-size:13px;line-height:22px}
.about-intro b{color:var(--navy)}
.pillar{top:330px;width:380px;text-align:center}
.pillar .icon{width:78px;height:78px;border-radius:50%;background:var(--grey-bg);margin:0 auto 18px;display:flex;align-items:center;justify-content:center}
.pillar h3{font-family:"Montserrat",Arial,sans-serif;font-weight:700;font-size:15px;color:var(--ink);margin-bottom:10px}
.pillar p{font-size:12.5px;line-height:21px;margin-bottom:22px;white-space:nowrap}
.about-divider{left:600px;top:340px;width:1px;height:270px;background:var(--line)}

/* services */
.services{top:1330px;height:900px;background:var(--grey-bg)}
.services .heading{top:190px}
.services .subheading{top:243px}
.services .dots{top:272px}
.services-intro{left:143px;top:300px;width:914px;text-align:center;font-size:13px;line-height:22px}
.service-card{top:430px;width:260px;height:260px;background:var(--white);box-shadow:0 4px 16px rgba(30,40,70,.1);text-align:center}
.service-card .photo{margin:10px;height:170px}
.service-card h4{font-family:"Montserrat",Arial,sans-serif;font-weight:600;font-size:13px;color:var(--ink);line-height:18px;margin-top:18px}
.service-card.featured::before,.service-card.featured::after{content:"";position:absolute;width:60px;height:60px;border:4px solid var(--navy)}
.service-card.featured::before{left:-10px;top:-10px;border-right:none;border-bottom:none}
.service-card.featured::after{right:-10px;bottom:-10px;border-left:none;border-top:none}
.services .btn{position:absolute;left:541px;top:750px}

/* equipment */
.equipment{top:2230px;height:860px}
.equipment .heading{top:95px}
.equipment .subheading{top:148px}
.equipment .dots{top:177px}
.tabs{left:143px;top:222px;width:917px;display:flex;border-bottom:1px solid var(--line);font-family:"Montserrat",Arial,sans-serif;font-weight:600;font-size:12px;color:var(--ink)}
.tabs span{flex:1;text-align:center;padding:12px 0}
.tabs .active{flex:0 0 80px;background:var(--white);box-shadow:0 -3px 10px rgba(0,0,0,.08)}
.equip-panel{left:143px;top:265px;width:917px;height:475px;background:var(--white);box-shadow:0 4px 18px rgba(30,40,70,.12)}
.equip-grid{position:absolute;left:20px;top:20px;display:grid;grid-template-columns:repeat(3,285px);grid-auto-rows:207px;gap:10px}
.equip-tile{position:relative;overflow:hidden}
.equip-tile .photo{position:absolute;inset:0}
.equip-tile .caption{position:absolute;left:0;right:0;bottom:0;padding:10px 40px 10px 14px;background:linear-gradient(transparent,rgba(10,20,50,.85));color:var(--white)}
.equip-tile h5{font-family:"Montserrat",Arial,sans-serif;font-weight:600;font-size:13px;line-height:17px}
.equip-tile p{font-size:11px;line-height:15px;opacity:.85}
.equip-tile svg{position:absolute;right:12px;bottom:14px}

/* industry */
.industry{top:3090px;height:670px;background:var(--grey-bg)}
.industry .heading{top:225px}
.industry .subheading{top:278px}
.industry .dots{top:306px}
.industry-item{top:330px;width:150px;text-align:center}
.industry-item .circle{width:118px;height:118px;border-radius:50%;background:var(--white);border:1px solid var(--line);margin:0 auto;display:flex;align-items:center;justify-content:center;box-shadow:0 3px 10px rgba(30,40,70,.08)}
.industry-item.active .circle{background:var(--navy);border-color:var(--navy)}
.industry-item span{display:block;margin-top:18px;font-family:"Montserrat",Arial,sans-serif;font-weight:600;font-size:13px;color:var(--ink)}
.arrow-btn{top:372px;width:34px;height:34px;border-radius:50%;background:var(--white);box-shadow:0 2px 8px rgba(0,0,0,.12);display:flex;align-items:center;justify-content:center}

/* quote */
.quote{top:3760px;height:508px}
.quote .heading{top:110px}
.quote .subheading{top:163px}
.quote .dots{top:192px}
.quote-form{left:270px;top:240px;width:660px;height:275px;background:var(--white);box-shadow:0 4px 20px rgba(30,40,70,.14);z-index:2}
.field{position:absolute;border:1px solid var(--line);font-size:11px;color:var(--muted);padding:7px 10px}
.quote-form .btn{position:absolute;left:282px;top:210px}

/* footer */
.site-footer{top:4268px;height:507px;background:var(--footer);color:var(--footer-text)}
.footer-brand{left:0;width:1200px;top:115px;display:flex;justify-content:center;align-items:center;gap:12px;font-family:"Montserrat",Arial,sans-serif;font-weight:700;font-size:22px;color:var(--white)}
.footer-brand i{width:30px;height:30px;border-radius:50%;border:3px solid var(--white);display:block}
.footer-col{top:220px;font-size:12px;line-height:26px}
.footer-col h6{font-family:"Montserrat",Arial,sans-serif;font-weight:700;font-size:13px;color:var(--white);margin-bottom:10px}
.links{display:grid;grid-template-columns:110px 100px}
.links span::before{content:"›";margin-right:8px;color:var(--white)}
.row{display:flex;align-items:center;gap:10px}
.row svg{flex:0 0 auto}
.badge{width:48px;height:48px;border-radius:50%;background:#4a6fc7}
.badge.square{border-radius:4px;background:#c9a23a}
.copyright{left:0;width:1200px;top:450px;border-top:1px solid #4c4f57;padding-top:14px;text-align:center;font-size:11px}
</style>
</head>
<body>

<section class="section hero">
  <div class="abs hero-photo" role="img" aria-label="Close-up photograph of a CNC machining spindle cutting a metal part"></div>
  <h1 class="abs hero-title">FROM BLUEPRINT<br>TO REALITY-<strong>BETTER THAN<br>YOU EXPECTED</strong></h1>
  <p class="abs hero-text">Lorem ipsum dolor sit amet, consectetuer adipiscing elit, sed diam nonummy nibh euismod tincidunt ut laoreet dolore.</p>
  <span class="btn">GET A QUOTE</span>
  <svg class="abs" style="left:0;top:470px" width="1200" height="170" viewBox="0 0 1200 170" preserveAspectRatio="none">
    <path d="M0 60 C300 190 800 190 1200 20 L1200 170 L0 170 Z" fill="#ffffff"/>
  </svg>
</section>

<header class="section site-header">
  <div class="abs brand"><i></i>Vardel Precision</div>
  <nav class="abs nav">
    <span class="active">HOME</span><span>ABOUT US</span><span>SERVICES</span><span>EQUIPMENT</span><span>QUALITY</span><span>OUR WORK</span><span>CONTACT</span>
    <span><svg width="12" height="12" viewBox="0 0 12 12"><circle cx="5" cy="5" r="3.8" fill="none" stroke="#3a3d45" stroke-width="1.6"/><path d="M8 8l3 3" stroke="#3a3d45" stroke-width="1.6"/></svg></span>
  </nav>
</header>

<section class="section about">
  <h2 class="abs heading">ABOUT <strong>US</strong></h2>
  <p class="abs subheading">Lorem ipsum dolor sit amet</p>
  <div class="abs dots"><span></span><span></span><span></span><span></span><span></span></div>
  <p class="abs about-intro"><b>VARDEL PRECISION MANUFACTURING</b> Company is a high quality machining resource providing friendly service, fast turnaround times, and engineering expertise at competitive pricing. With almost 20 years of experience in the industry, Vardel Precision utilizes certified state of the art equipment partnered with top professionals to maximize the value and quality in your product.</p>
  <div class="abs pillar" style="left:182px">
    <div class="icon"><svg width="36" height="36" viewBox="0 0 36 36" fill="none" stroke="#1f3b8c" stroke-width="2"><circle cx="17" cy="19" r="13"/><circle cx="17" cy="19" r="8"/><circle cx="17" cy="19" r="3"/><path d="M17 19L31 5M26 5h5v5"/></svg></div>
    <h3>OUR MISSION</h3>
    <p>Our mission is to provide customers<br>with reliable and expert service, using state of the art<br>equipment, to benefit their business, and creating<br>lasting relationships thereafter.</p>
    <span class="btn">LEARN MORE</span>
  </div>
  <div class="abs about-divider"></div>
  <div class="abs pillar" style="left:644px">
    <div class="icon"><svg width="38" height="28" viewBox="0 0 38 28" fill="none" stroke="#1f3b8c" stroke-width="2"><path d="M2 14C9 3 29 3 36 14C29 25 9 25 2 14Z"/><circle cx="19" cy="14" r="6"/><circle cx="19" cy="14" r="2" fill="#1f3b8c"/></svg></div>
    <h3>OUR VISION</h3>
    <p>Ut wisi enim ad minim veniam, quis nostrud<br>exerci tation ullamcorper suscipit lobortis nisl ut aliquip ex<br>ea commodo consequat at vero eros et<br>accumsan et iusto odio.</p>
    <span class="btn">LEARN MORE</span>
  </div>
</section>

<section class="section services">
  <svg class="abs" style="left:0;top:-10px" width="1200" height="150" viewBox="0 0 1200 150" preserveAspectRatio="none">
    <path d="M0 0 H1200 V30 C900 150 400 150 0 40 Z" fill="#ffffff"/>
    <path d="M700 118 C900 100 1080 60 1200 10 L1200 24 C1080 75 900 112 700 118 Z" fill="#1f3b8c"/>
  </svg>
  <h2 class="abs heading">OUR <strong>SERVICES</strong></h2>
  <p class="abs subheading">Lorem ipsum dolor sit amet</p>
  <div class="abs dots"><span></span><span></span><span></span><span></span><span></span></div>
  <p class="abs services-intro">Providing you with honest straightforward service is our number one goal. We manufacture finished metal and plastic goods to tight tolerances using technologically advanced equipment. Our spotlight is multi-featured products manufactured on 7 plus axis world-class screw machines. Our ideal sizes, not our limits, are from .02 to 1.25 inches diameter by .050 to 5.00 inches in length. Cross holes, wrench flats or something new to us all, completed in one operation. Whether you need to make one or a million our screw machine department is capable of fulfilling your need.</p>
  <div class="abs service-card" style="left:150px">
    <div class="photo" role="img" aria-label="Photograph of a machined metal part in production" style="background:linear-gradient(135deg,#6b6e74,#2f3137)"></div>
    <h4>PART<br>PRODUCTION</h4>
  </div>
  <div class="abs service-card featured" style="left:470px">
    <div class="photo" role="img" aria-label="Photograph of engineers reviewing a machine together" style="background:linear-gradient(135deg,#5d7fb4,#d9b24a)"></div>
    <h4>ENGINEERING<br>ASSISTANCE</h4>
  </div>
  <div class="abs service-card" style="left:790px">
    <div class="photo" role="img" aria-label="Photograph of a technician at a computer beside a machine" style="background:linear-gradient(135deg,#e3e7ec,#8795a8)"></div>
    <h4>OUTSIDE PROCESS<br>COORDINATION</h4>
  </div>
  <span class="btn">LEARN MORE</span>
  <svg class="abs" style="left:0;top:720px" width="1200" height="190" viewBox="0 0 1200 190" preserveAspectRatio="none">
    <path d="M0 190 V130 C300 30 700 60 1200 150 V190 Z" fill="#ffffff"/>
    <path d="M0 150 C150 90 330 60 480 62 C330 72 160 110 0 168 Z" fill="#1f3b8c"/>
  </svg>
</section>

<section class="section equipment">
  <h2 class="abs heading">OUR <strong>EQUIPMENTS</strong></h2>
  <p class="abs subheading">Lorem ipsum dolor sit amet</p>
  <div class="abs dots"><span></span><span></span><span></span><span></span><span></span></div>
  <div class="abs tabs"><span class="active">ALL</span><span>SUPPORT EQUIPMENT</span><span>QA EQUIPMENT</span><span>MACHINE EQUIPMENT</span></div>
  <div class="abs equip-panel">
    <div class="equip-grid">
      <div class="equip-tile"><div class="photo" role="img" aria-label="Photograph of a row of CNC screw machines" style="background:linear-gradient(135deg,#9aa7b8,#3c4a63)"></div><div class="caption"><h5>CNC Screw Machines</h5><p>Manufacture 7 plus axis machining at its best. We offer...</p></div><svg width="16" height="16" viewBox="0 0 16 16"><circle cx="8" cy="8" r="7" fill="none" stroke="#fff" stroke-width="1.4"/><path d="M6.5 5l3 3-3 3" fill="none" stroke="#fff" stroke-width="1.4"/></svg></div>
      <div class="equip-tile"><div class="photo" role="img" aria-label="Photograph of a CNC lathe turn center" style="background:linear-gradient(135deg,#707680,#23262c)"></div><div class="caption"><h5>CNC Lathes - Mill / Turn Centers</h5><p>Multi Axis CNC Mill / Turn Centers - Each with multiple spindles...</p></div><svg width="16" height="16" viewBox="0 0 16 16"><circle cx="8" cy="8" r="7" fill="none" stroke="#fff" stroke-width="1.4"/><path d="M6.5 5l3 3-3 3" fill="none" stroke="#fff" stroke-width="1.4"/></svg></div>
      <div class="equip-tile"><div class="photo" role="img" aria-label="Photograph of CNC machining centers on a shop floor" style="background:linear-gradient(135deg,#b9b6ad,#5b5c60)"></div><div class="caption"><h5>CNC Machining Centers</h5><p>Horizontal and Vertical. Here are examples of a few of our...</p></div><svg width="16" height="16" viewBox="0 0 16 16"><circle cx="8" cy="8" r="7" fill="none" stroke="#fff" stroke-width="1.4"/><path d="M6.5 5l3 3-3 3" fill="none" stroke="#fff" stroke-width="1.4"/></svg></div>
      <div class="equip-tile"><div class="photo" role="img" aria-label="Photograph of a gantry coordinate measuring machine" style="background:linear-gradient(135deg,#c9ced6,#6d7584)"></div><div class="caption"><h5>Kestrel Vista 400 DCC CMM</h5><p>Vision and Contact CMM Measuring Capabilities...</p></div><svg width="16" height="16" viewBox="0 0 16 16"><circle cx="8" cy="8" r="7" fill="none" stroke="#fff" stroke-width="1.4"/><path d="M6.5 5l3 3-3 3" fill="none" stroke="#fff" stroke-width="1.4"/></svg></div>
      <div class="equip-tile"><div class="photo" role="img" aria-label="Photograph of an optical comparator screen" style="background:radial-gradient(circle at 50% 40%,#e6e8ea,#4a4d52 70%)"></div><div class="caption"><h5>Optical Comparator</h5><p>Digital w/ Geometric Function and Optical Edge Find ability</p></div><svg width="16" height="16" viewBox="0 0 16 16"><circle cx="8" cy="8" r="7" fill="none" stroke="#fff" stroke-width="1.4"/><path d="M6.5 5l3 3-3 3" fill="none" stroke="#fff" stroke-width="1.4"/></svg></div>
      <div class="equip-tile"><div class="photo" role="img" aria-label="Photograph of an orange horizontal band saw" style="background:linear-gradient(135deg,#e36a2a,#5a2a14)"></div><div class="caption"><h5>CNC Programmable Horizontal Sawing</h5><p>Vertical Sawing - 18"-24" Capacity. Various Manual Equipment for...</p></div><svg width="16" height="16" viewBox="0 0 16 16"><circle cx="8" cy="8" r="7" fill="none" stroke="#fff" stroke-width="1.4"/><path d="M6.5 5l3 3-3 3" fill="none" stroke="#fff" stroke-width="1.4"/></svg></div>
    </div>
  </div>
</section>

<section class="section industry">
  <svg class="abs" style="left:0;top:0" width="1200" height="170" viewBox="0 0 1200 170" preserveAspectRatio="none">
    <path d="M0 0 H1200 V20 C850 170 350 150 0 100 Z" fill="#ffffff"/>
    <path d="M720 150 C900 130 1080 80 1200 20 L1200 36 C1080 95 900 140 720 150 Z" fill="#1f3b8c"/>
  </svg>
  <h2 class="abs heading">INDUSTRY <strong>WE SERVE</strong></h2>
  <p class="abs subheading">Lorem ipsum dolor sit amet diam nonummy nibh</p>
  <div class="abs dots"><span></span><span></span><span></span><span></span><span></span></div>
  <div class="abs arrow-btn" style="left:70px"><svg width="10" height="12" viewBox="0 0 10 12"><path d="M7 1L2 6l5 5" fill="none" stroke="#3a3d45" stroke-width="1.8"/></svg></div>
  <div class="abs arrow-btn" style="left:1096px"><svg width="10" height="12" viewBox="0 0 10 12"><path d="M3 1l5 5-5 5" fill="none" stroke="#3a3d45" stroke-width="1.8"/></svg></div>
  <div class="abs industry-item" style="left:132px"><div class="circle"><svg width="56" height="56" viewBox="0 0 56 56" fill="none" stroke="#1f3b8c" stroke-width="2.5"><circle cx="28" cy="28" r="24"/><circle cx="28" cy="28" r="8"/><path d="M5 24h15M36 24h15M28 36v16"/></svg></div><span>AUTOMOTIVE</span></div>
  <div class="abs industry-item" style="left:329px"><div class="circle"><svg width="50" height="56" viewBox="0 0 50 56" fill="none" stroke="#1f3b8c" stroke-width="2.5"><circle cx="25" cy="8" r="5"/><path d="M25 13v40M14 20h22M4 34c2 12 11 19 21 19s19-7 21-19M1 38l3-5 5 4M49 38l-3-5-5 4"/></svg></div><span>MARINE</span></div>
  <div class="abs industry-item active" style="left:523px"><div class="circle"><svg width="44" height="58" viewBox="0 0 44 58" fill="none" stroke="#ffffff" stroke-width="2.5"><path d="M22 2C31 11 32 24 30 40H14C12 24 13 11 22 2Z"/><circle cx="22" cy="20" r="4"/><path d="M14 30L5 42l9-2M30 30l9 12-9-2M18 46l-2 8M22 46v10M26 46l2 8"/></svg></div><span>AEROSPACE</span></div>
  <div class="abs industry-item" style="left:720px"><div class="circle"><svg width="56" height="56" viewBox="0 0 56 56" fill="none" stroke="#1f3b8c" stroke-width="2.2"><rect x="18" y="18" width="20" height="20" rx="2"/><path d="M28 18V8M22 18v-6l-8-6M34 18v-6l8-6M38 28h12M38 24h6l6-6M18 28H6M18 34h-6l-6 6M28 38v12M34 38v6l6 6"/><circle cx="28" cy="6" r="2"/><circle cx="52" cy="28" r="2"/><circle cx="4" cy="28" r="2"/></svg></div><span>ELECTRONICS</span></div>
  <div class="abs industry-item" style="left:917px"><div class="circle"><svg width="60" height="44" viewBox="0 0 60 44" fill="none" stroke="#1f3b8c" stroke-width="2.5"><rect x="9" y="4" width="42" height="28" rx="2"/><path d="M2 36h56l-4 5H6Z"/></svg></div><span>COMPUTER</span></div>
  <svg class="abs" style="left:0;top:520px" width="1200" height="150" viewBox="0 0 1200 150" preserveAspectRatio="none">
    <path d="M0 150 V110 C300 20 750 40 1200 130 V150 Z" fill="#ffffff"/>
    <path d="M0 128 C150 70 330 40 480 42 C330 52 160 90 0 146 Z" fill="#1f3b8c"/>
  </svg>
</section>

<section class="section quote">
  <h2 class="abs heading">REQUEST <strong>A QUOTE</strong></h2>
  <p class="abs subheading">Lorem ipsum dolor sit amet diam nonummy nibh</p>
  <div class="abs dots"><span></span><span></span><span></span><span></span><span></span></div>
  <form class="abs quote-form">
    <div class="field" style="left:55px;top:40px;width:270px;height:34px">Name</div>
    <div class="field" style="left:335px;top:40px;width:270px;height:34px">Email</div>
    <div class="field" style="left:55px;top:86px;width:550px;height:90px">Request</div>
    <span class="btn">SUBMIT</span>
  </form>
</section>

<footer class="section site-footer">
  <div class="abs footer-brand"><i></i>Vardel Precision</div>
  <div class="abs footer-col" style="left:143px">
    <h6>QUICK LINKS</h6>
    <div class="links"><span>Home</span><span>Our Work</span><span>Services</span><span>About Us</span><span>Equipment</span><span>Contact</span><span>Quality</span><span>Site Map</span></div>
  </div>
  <div class="abs footer-col" style="left:400px">
    <h6>CONTACT DETAILS</h6>
    <div class="row" style="align-items:flex-start;line-height:17px;margin-bottom:8px"><svg width="12" height="16" viewBox="0 0 12 16"><path d="M6 15C2 10 1 8 1 6a5 5 0 0110 0c0 2-1 4-5 9Z" fill="#c9ccd2"/><circle cx="6" cy="6" r="2" fill="#3b3e46"/></svg><span><b style="color:#fff">VARDEL PRECISION MANUFACTURING</b><br>4120 Calder Way, Brookhaven,<br>CA 90000</span></div>
    <div class="row"><svg width="12" height="12" viewBox="0 0 12 12"><path d="M2 1h3l1 3-2 1c1 2 2 3 4 4l1-2 3 1v3c-6 0-10-4-10-10Z" fill="#c9ccd2"/></svg>555-014-2270</div>
    <div class="row"><svg width="12" height="12" viewBox="0 0 12 12"><rect x="1" y="2" width="10" height="8" fill="#c9ccd2"/><path d="M3 4h6M3 6h6" stroke="#3b3e46"/></svg>555-014-2271</div>
    <div class="row"><svg width="12" height="10" viewBox="0 0 12 10"><rect x="0.5" y="0.5" width="11" height="9" fill="none" stroke="#c9ccd2"/><path d="M1 1l5 4 5-4" fill="none" stroke="#c9ccd2"/></svg>info@vardelprecisionmachining.example</div>
  </div>
  <div class="abs footer-col" style="left:675px">
    <h6>FOLLOW US ON</h6>
    <div class="row"><svg width="14" height="14"><rect width="14" height="14" rx="2" fill="#5b5f69"/></svg>Community</div>
    <div class="row"><svg width="14" height="14"><rect width="14" height="14" rx="2" fill="#5b5f69"/></svg>Gallery</div>
    <div class="row"><svg width="14" height="14"><rect width="14" height="14" rx="2" fill="#5b5f69"/></svg>Updates</div>
    <div class="row"><svg width="14" height="14"><rect width="14" height="14" rx="2" fill="#5b5f69"/></svg>Network</div>
  </div>
  <div class="abs footer-col" style="left:897px">
    <h6>ACCREDITATION</h6>
    <div class="row" style="gap:14px;margin-top:8px">
      <svg width="8" height="12" viewBox="0 0 8 12"><path d="M6 1L1 6l5 5" fill="none" stroke="#fff" stroke-width="1.6"/></svg>
      <div class="badge"></div><div class="badge square"></div>
      <svg width="8" height="12" viewBox="0 0 8 12"><path d="M2 1l5 5-5 5" fill="none" stroke="#fff" stroke-width="1.6"/></svg>
    </div>
  </div>
  <p class="abs copyright">© 2018 Vardel Precision Manufacturing. All Rights Reserved.</p>
</footer>

</body>
</html>
```